Mobile App UI for Telecommunications/Hosting Company

We are about to convert our existing self-service Customer Portal into a mobile phone application and need an elegant and professional UI/UX design. Our company provides telecommunication (voice/mobile/data) and hosting services to medium-sized business. The primary purpose of the application is to view trouble tickets, alerts, orders, and performance charts. This application is available to customers only - not the general public.

Please provide a UI design suitable for display on iPhone/Android devices. The attached document includes a proposed screen flow. You are free to design your own screens to display the same information elegantly.
Updates

Please note that the design should be based on the wireframes in the Word document, not the screenshots.  The screenshots are just to show our existing web portal look & feel.

Also, just a few screens are required for initial submission (3 would be great).

Thanks,
Dermot.

Target Market(s)

IT Managers away from their desk and using a mobile phone application.
Adult males from technical background aged 30-50.
Customers of Brindlewood Networks have access to this application (not the general public). This is a self-service portal for customers only.

Industry/Entity Type

Business

Colors
0592cd
33a6d7
85cae6
cadf82
fde08a

Requirements
Must have
• Please look at the screenshots from our current Customer Portal site (part of the project brief). The mobile app does not have to look the same, but should follow a similar style.

Please check out our company web site at www.brindlewoodnetworks.example (this site is not the customer portal and has a different look at feel) to understand what Brindlewood Networks does.
Nice to have
• Sharing capabilities via email/SMS.
A nice background image to make it stand out
The colours selected below are a guide only as they are similar to the corporate colours
- The priority is something that works on a phone - a design extendable to tablets is a nice to have as our existing web site looks OK on a tablet..

```html
<!DOCTYPE html>
<html lang="en">
<head>
<meta charset="utf-8">
<title>linkpane – Mobile App Screens</title>
<link href="https://fonts.googleapis.com/css2?family=Open+Sans:wght@400;600;700&display=swap" rel="stylesheet">
<style>
  :root {
    --page: #ffffff;
    --panel: #f7f7f7;
    --panel-dark: #2b2f33;
    --panel-teal: #54c3d4;
    --screen: #ffffff;
    --screen-edge: #2a2a2a;
    --brand-blue: #1a73c9;
    --brand-sky: #33a6d7;
    --button: #3cb8ea;
    --ink-soft: #8a8f94;
    --ink-faint: #b4b8bc;
    --field-line: #e3e5e7;
    --status-bar: #111111;
    --icon-navy: #1f4f9c;
    --icon-teal: #55c3d6;
    --icon-lime: #cadf82;
    --illustration: #dcdddf;
  }
  * { box-sizing: border-box; margin: 0; padding: 0; }
  html, body { width: 1200px; height: 572px; overflow: hidden; }
  body {
    background: var(--page);
    font-family: "Open Sans", Arial, sans-serif;
    position: relative;
  }

  /* presentation panels */
  .panel {
    position: absolute; top: 48px; width: 320px; height: 500px;
    background: var(--panel); overflow: hidden;
  }
  .panel--splash { left: 58px; }
  .panel--login-a { left: 441px; }
  .panel--login-b { left: 824px; }
  .panel__band { position: absolute; inset: 0; }
  .panel__band--dark { background: var(--panel-dark); clip-path: polygon(58% 0, 100% 0, 100% 20%); }
  .panel__band--teal { background: var(--panel-teal); clip-path: polygon(0 50%, 100% 95%, 100% 100%, 0 100%); }
  .panel--login-a .panel__band--teal,
  .panel--login-b .panel__band--teal { clip-path: polygon(0 50%, 100% 96%, 100% 100%, 0 100%); }
  .panel--login-a .panel__band--dark,
  .panel--login-b .panel__band--dark { clip-path: polygon(58% 0, 100% 0, 100% 19%); }

  /* phone screens */
  .screen {
    position: absolute;
    background: var(--screen);
    height: 230px;
    border: 2px solid var(--screen-edge);
    border-radius: 2px;
    overflow: hidden;
  }
  .screen--splash { left: 106px; top: 155px; width: 132px; }
  .screen--login-a { left: 535px; top: 150px; width: 127px; }
  .screen--login-b { left: 918px; top: 150px; width: 132px; }

  .status-bar {
    position: relative;
    height: 9px;
    background: var(--status-bar);
    color: #fff;
    font-size: 4px;
    display: flex;
    justify-content: space-between;
    align-items: center;
    padding: 0 3px;
  }
  .status-bar .time { position: absolute; left: 50%; transform: translateX(-50%); }

  .brand-mark {
    width: 26px; height: 26px; border-radius: 50%;
    background: linear-gradient(135deg, var(--brand-sky), var(--brand-blue));
    margin: 0 auto;
  }
  .brand-name {
    color: var(--brand-blue);
    font-weight: 400;
    text-align: center;
    letter-spacing: 0.2px;
  }

  .splash-brand { position: absolute; top: 52px; left: 0; right: 0; }
  .splash-brand .brand-mark { width: 36px; height: 36px; }
  .splash-brand .brand-name { font-size: 13px; margin-top: 8px; }

  .welcome {
    color: var(--ink-soft);
    font-size: 6px;
    text-align: center;
    font-weight: 600;
    line-height: 1.3;
  }
  .login-form { position: absolute; left: 11px; right: 11px; }
  .field {
    height: 15px;
    border: 1px solid var(--field-line);
    border-radius: 2px;
    font-size: 3.5px;
    color: var(--ink-faint);
    padding: 0 3px 0 4px;
    display: flex; align-items: center; justify-content: space-between;
    margin-bottom: 4px;
  }
  .field svg { width: 7px; height: 7px; }
  .login-button {
    display: block;
    height: 16px;
    background: var(--button);
    color: #fff;
    font-size: 6px;
    font-weight: 600;
    text-align: center;
    line-height: 16px;
    border-radius: 1px;
    margin-top: 5px;
  }
  .form-notes {
    position: absolute; left: 0; right: 0;
    text-align: center; font-size: 3.5px; color: var(--ink-soft); line-height: 1.6;
  }
  .form-notes .help { color: var(--brand-sky); font-weight: 600; }

  .screen--login-a .welcome { position: absolute; top: 25px; left: 0; right: 0; }
  .screen--login-a .login-brand { position: absolute; top: 52px; left: 0; right: 0; }
  .screen--login-a .login-brand .brand-mark { width: 30px; height: 30px; }
  .screen--login-a .login-brand .brand-name { font-size: 11px; margin-top: 6px; }
  .screen--login-a .login-form { top: 125px; }
  .screen--login-a .form-notes { top: 198px; }

  .screen--login-b .login-brand {
    position: absolute; top: 34px; left: 0; right: 0;
    display: flex; justify-content: center; align-items: center; gap: 4px;
  }
  .screen--login-b .login-brand .brand-mark { width: 14px; height: 14px; margin: 0; }
  .screen--login-b .login-brand .brand-name { font-size: 10px; }
  .screen--login-b .welcome { position: absolute; top: 76px; left: 0; right: 0; font-weight: 400; font-size: 5px; }
  .screen--login-b .login-form { top: 106px; }
  .screen--login-b .form-notes { top: 189px; }

  /* decorative network art, left as soft placeholders */
  .network-art { position: absolute; background: var(--illustration); opacity: 0.55; border-radius: 30px; }
  .network-art--nodes { left: 58px; top: 62px; width: 100px; height: 58px; }
  .network-art--people { left: 238px; top: 82px; width: 64px; height: 64px; }
  .network-art--cloud { left: 272px; top: 155px; width: 90px; height: 105px; border-radius: 40px 40px 10px 10px; }

  .app-icons-title {
    position: absolute; left: 287px; top: 283px;
    color: var(--brand-sky); font-size: 12px; font-weight: 600;
  }
  .app-icon {
    position: absolute; width: 34px; height: 34px; border-radius: 8px;
    display: flex; align-items: center; justify-content: center;
  }
  .app-icon::after {
    content: ""; width: 17px; height: 17px; border-radius: 50%;
    background: linear-gradient(135deg, var(--brand-sky), var(--brand-blue));
  }
  .app-icon--outline { left: 330px; top: 309px; border: 2px solid var(--icon-navy); background: #fff; }
  .app-icon--teal { left: 295px; top: 355px; background: var(--icon-teal); }
  .app-icon--teal::after { background: linear-gradient(135deg, #ffffff, #bfe6f3); }
  .app-icon--ring { left: 330px; top: 396px; border-radius: 50%; border: 2px solid var(--icon-lime); background: #fff; }
  .app-icon--navy { left: 305px; top: 440px; background: var(--icon-navy); }
  .app-icon--navy::after { background: linear-gradient(135deg, #8fd3f0, var(--brand-sky)); }
</style>
</head>
<body>

  <div class="panel panel--splash"><div class="panel__band panel__band--dark"></div><div class="panel__band panel__band--teal"></div></div>
  <div class="panel panel--login-a"><div class="panel__band panel__band--dark"></div><div class="panel__band panel__band--teal"></div></div>
  <div class="panel panel--login-b"><div class="panel__band panel__band--dark"></div><div class="panel__band panel__band--teal"></div></div>

  <div class="network-art network-art--nodes" role="img" aria-label="Light grey linked network nodes"></div>
  <div class="network-art network-art--people" role="img" aria-label="Light grey connected user avatars"></div>
  <div class="network-art network-art--cloud" role="img" aria-label="Light grey cloud with data arrows"></div>

  <section class="screen screen--splash" aria-label="Splash screen">
    <div class="splash-brand">
      <div class="brand-mark"></div>
      <p class="brand-name">linkpane</p>
    </div>
  </section>

  <p class="app-icons-title">App Icon</p>
  <div class="app-icon app-icon--outline" role="img" aria-label="App icon, outlined"></div>
  <div class="app-icon app-icon--teal" role="img" aria-label="App icon, teal"></div>
  <div class="app-icon app-icon--ring" role="img" aria-label="App icon, round"></div>
  <div class="app-icon app-icon--navy" role="img" aria-label="App icon, navy"></div>

  <section class="screen screen--login-a" aria-label="Login screen, centred layout">
    <div class="status-bar"><span>CARRIER</span><span class="time">4:21 PM</span><span>▮▮</span></div>
    <p class="welcome">Welcome to<br>linkpane!</p>
    <div class="login-brand">
      <div class="brand-mark"></div>
      <p class="brand-name">linkpane</p>
    </div>
    <form class="login-form">
      <div class="field">Username
        <svg viewBox="0 0 10 10"><circle cx="5" cy="3" r="2" fill="none" stroke="#bbb" stroke-width=".8"/><path d="M1 10c0-3 2-4 4-4s4 1 4 4" fill="none" stroke="#bbb" stroke-width=".8"/></svg>
      </div>
      <div class="field">Password
        <svg viewBox="0 0 10 10"><rect x="2" y="4.5" width="6" height="5" fill="none" stroke="#bbb" stroke-width=".8"/><path d="M3.3 4.5V3a1.7 1.7 0 0 1 3.4 0v1.5" fill="none" stroke="#bbb" stroke-width=".8"/></svg>
      </div>
      <span class="login-button">LOG IN</span>
    </form>
    <p class="form-notes">Remember me on this computer<br><span class="help">Need help logging in?</span></p>
  </section>

  <section class="screen screen--login-b" aria-label="Login screen, compact layout">
    <div class="status-bar"><span>CARRIER</span><span class="time">4:21 PM</span><span>▮▮</span></div>
    <div class="login-brand">
      <div class="brand-mark"></div>
      <p class="brand-name">linkpane</p>
    </div>
    <p class="welcome">Welcome to linkpane!</p>
    <form class="login-form">
      <div class="field">Username
        <svg viewBox="0 0 10 10"><circle cx="5" cy="3" r="2.2" fill="#aaa"/><path d="M1 10c0-3 2-4.5 4-4.5s4 1.5 4 4.5z" fill="#aaa"/></svg>
      </div>
      <div class="field">Password
        <svg viewBox="0 0 10 10"><rect x="2" y="4.5" width="6" height="5" fill="#aaa"/><path d="M3.3 4.5V3a1.7 1.7 0 0 1 3.4 0v1.5" fill="none" stroke="#aaa" stroke-width=".9"/></svg>
      </div>
      <span class="login-button">LOG IN</span>
    </form>
    <p class="form-notes">Remember me on this computer<br><span class="help">Need help logging in?</span></p>
  </section>

</body>
</html>
```